Product Insert / Thank You

I'm looking for a small card to be designed that will be included with our product when it ships. It will be 2 sided with 1 side being a "thank you" with our logo and the other side containing the following text:We would love to hear your feedback! For every review we receive on our products, we donate 100% of the proceeds of your order to TIDEWELL -- a non profit organization dedicated to preserving our oceans!If you are not 100% satisfied with your purchase or have any problems, we will always resolve your issue. please contact us via Brisko if you need assistance.Insert needs to be well organized and information presented in a clear and visually appealing way.
Target Market(s)
Women, aged 24-45
Colors
Designer to choose colors to be used in the design.
Look and feel
Each slider illustrates characteristics of the customer's brand and the style your logo design should communicate.

```html
<!DOCTYPE html>
<html lang="en">
<head>
<meta charset="utf-8">
<title>Alderway – Thank You Insert</title>
<link rel="stylesheet" href="https://fonts.googleapis.com/css2?family=Oswald:wght@700&family=PT+Sans+Narrow:wght@400;700&display=swap">
<style>
  :root {
    --backdrop: #2b2e33;
    --ink: #0b0b0b;
    --paper: #ffffff;
    --mid-grey: #6f6f6f;
    --dot-grey: #9a9a9a;
    --shadow: rgba(0,0,0,0.45);
  }
  * { box-sizing: border-box; margin: 0; padding: 0; }
  html, body {
    width: 1200px; height: 900px; overflow: hidden;
    background: var(--backdrop);
  }
  .sheet {
    position: relative; width: 1200px; height: 900px;
    display: flex; align-items: center; justify-content: center; gap: 40px;
  }
  .card {
    position: relative; width: 540px; height: 300px;
    overflow: hidden; box-shadow: 0 18px 40px var(--shadow);
  }

  /* Front */
  .card-front { background: var(--ink); }
  .card-front svg { position: absolute; inset: 0; }
  .thank-you {
    position: absolute; left: 0; right: 0; top: 92px;
    text-align: center;
    font-family: "Oswald", "Arial Narrow", sans-serif;
    font-weight: 700; font-size: 92px; line-height: 1;
    letter-spacing: 1px; color: var(--ink);
    text-shadow: 3px 3px 0 #bdbdbd;
  }

  /* Back */
  .card-back { background: var(--paper); font-family: "PT Sans Narrow", "Arial Narrow", sans-serif; }
  .back-band {
    position: absolute; left: 0; right: 0; top: 62px; height: 178px;
    background: var(--ink);
  }
  .rule { position: absolute; left: 0; right: 0; height: 2px; }
  .rule-top { top: 40px; background: var(--ink); }
  .rule-bottom { top: 218px; background: var(--paper); left: 18px; right: 18px; }
  .brand-seal {
    position: absolute; left: 50%; top: 22px; transform: translateX(-50%);
    width: 84px; height: 84px; border-radius: 50%;
    background: var(--paper); border: 4px solid var(--ink);
    display: flex; align-items: center; justify-content: center;
  }
  .brand-name {
    font-weight: 700; font-size: 17px; letter-spacing: 1px; color: var(--ink);
  }
  .back-copy {
    position: absolute; left: 30px; right: 30px; top: 112px;
    text-align: center; color: var(--paper);
    font-size: 14px; line-height: 1.3;
  }
  .back-copy strong { font-weight: 700; }
  .contact-line {
    position: absolute; left: 0; right: 0; top: 226px;
    text-align: center; color: var(--paper);
    font-style: italic; font-weight: 700; font-size: 13px;
  }
</style>
</head>
<body>
<main class="sheet">
  <section class="card card-front" aria-label="Thank you side">
    <svg width="540" height="300" viewBox="0 0 540 300">
      <polygon points="0,0 300,0 110,150 0,150" fill="var(--mid-grey)"/>
      <polygon points="60,60 480,60 540,150 480,240 60,240 0,150" fill="var(--paper)"/>
      <rect x="330" y="200" width="210" height="100" fill="var(--dot-grey)" role="img" aria-label="Halftone dot pattern"/>
      <polygon points="60,240 480,240 520,180 540,180 540,300 0,300 0,150" fill="var(--ink)" opacity="0"/>
      <line x1="80" y1="78" x2="460" y2="78" stroke="var(--ink)" stroke-width="2"/>
      <line x1="80" y1="222" x2="460" y2="222" stroke="var(--ink)" stroke-width="2"/>
    </svg>
    <div class="thank-you">THANK YOU</div>
  </section>

  <section class="card card-back" aria-label="Message side">
    <div class="back-band"></div>
    <div class="rule rule-top"></div>
    <div class="rule rule-bottom"></div>
    <div class="brand-seal"><span class="brand-name">ALDERWAY</span></div>
    <p class="back-copy">
      We would love to hear your feedback!<br>
      For every review we receive on our products, we donate <strong>100%</strong> of the proceeds of your
      order to <strong>TIDEWELL</strong> – a non profit organization dedicated to preserving our oceans!<br>
      If you are not <strong>100%</strong> satisfied with your purchase or have any problems,<br>
      we will always resolve your issue.
    </p>
    <p class="contact-line">Please Contact Us Via Brisko If You Need Assistance.</p>
  </section>
</main>
</body>
</html>
```